To create online free mini games website. There’re will be up to 100 games on website with 6-8 categories. Domain name is not selected yet.

Number of Pages Required

1 page

```html
<!DOCTYPE html>
<html lang="en">
<head>
<meta charset="utf-8">
<title>Arcadia Mini – Free Mini Games</title>
<link rel="stylesheet" href="https://fonts.googleapis.com/css2?family=Fredoka:wght@500;600&family=Nunito:wght@600;800&display=swap">
<style>
  :root {
    --yellow: #f2b619;
    --yellow-dark: #d99a0c;
    --maroon: #7a1a22;
    --maroon-dark: #5a1016;
    --ink: #2a2a33;
    --page: #eeeeee;
    --card: #ffffff;
    --blue: #3a7bd5;
    --orange: #ef7b22;
    --green: #4caf3e;
    --purple: #6a4bc4;
    --red: #d8393c;
    --teal: #1fa5a0;
  }
  * { box-sizing: border-box; margin: 0; padding: 0; }
  html, body { width: 1200px; height: 800px; overflow: hidden; }
  body { background: var(--page); font-family: "Nunito", sans-serif; color: var(--ink); }

  .site-header {
    height: 60px; background: var(--yellow);
    display: flex; align-items: center; justify-content: space-between;
    padding: 0 24px; border-bottom: 4px solid var(--yellow-dark);
  }
  .brand { display: flex; align-items: center; gap: 10px; }
  .brand-mark { width: 22px; height: 22px; border-radius: 50%; background: var(--maroon); }
  .brand-name { font-family: "Fredoka", sans-serif; font-weight: 600; font-size: 26px; color: var(--maroon); }
  .main-nav { display: flex; gap: 8px; }
  .main-nav a {
    text-decoration: none; color: #fff; background: var(--ink);
    font-weight: 800; font-size: 14px; padding: 8px 16px; border-radius: 4px;
  }

  .hero {
    height: 220px; position: relative;
    background: linear-gradient(120deg, #3b2a7a 0%, #6b3fb8 45%, #8f5bd6 70%, #4a8f6a 100%);
  }
  .hero-copy { position: absolute; left: 40px; top: 40px; color: #fff; }
  .hero-tag {
    display: inline-block; background: var(--yellow); color: var(--maroon);
    font-weight: 800; font-size: 13px; padding: 4px 10px; border-radius: 3px; letter-spacing: 1px;
  }
  .hero-title { font-family: "Fredoka", sans-serif; font-weight: 600; font-size: 48px; margin: 12px 0 14px; white-space: nowrap; }
  .hero-btn {
    display: inline-block; background: var(--orange); color: #fff; font-weight: 800;
    font-size: 16px; padding: 10px 24px; border-radius: 4px;
  }

  .content { height: 440px; display: flex; gap: 20px; padding: 20px; }
  .category-list { width: 180px; display: flex; flex-direction: column; gap: 8px; }
  .category-list h2, .games h2 {
    font-family: "Fredoka", sans-serif; font-weight: 600; font-size: 20px; height: 30px;
  }
  .category {
    color: #fff; font-weight: 800; font-size: 15px; padding: 0 14px;
    height: 52px; display: flex; align-items: center; border-radius: 4px;
  }
  .cat-blue { background: var(--blue); }
  .cat-orange { background: var(--orange); }
  .cat-green { background: var(--green); }
  .cat-purple { background: var(--purple); }
  .cat-red { background: var(--red); }
  .cat-teal { background: var(--teal); }

  .games { flex: 1; display: flex; flex-direction: column; gap: 8px; }
  .game-grid { flex: 1; display: grid; grid-template-columns: repeat(6, 1fr); grid-template-rows: 1fr 1fr; gap: 12px; }
  .game-card {
    background: var(--card); border-radius: 4px; overflow: hidden;
    display: flex; flex-direction: column; box-shadow: 0 1px 3px rgba(0,0,0,.15);
  }
  .game-thumb { height: 110px; }
  .game-info { flex: 1; display: flex; align-items: center; justify-content: space-between; gap: 6px; padding: 0 10px; }
  .game-title { font-size: 13px; font-weight: 800; white-space: nowrap; }
  .game-play {
    font-size: 12px; font-weight: 800; color: #fff; background: var(--maroon);
    padding: 4px 8px; border-radius: 3px; flex-shrink: 0;
  }
  .t1 { background: linear-gradient(135deg, #f6c945, #e77b2b); }
  .t2 { background: linear-gradient(135deg, #5fb3e8, #2f6fb5); }
  .t3 { background: linear-gradient(135deg, #8ed36a, #3f9a3a); }
  .t4 { background: linear-gradient(135deg, #b58de8, #5a3ca8); }
  .t5 { background: linear-gradient(135deg, #f08a7a, #c23a3a); }
  .t6 { background: linear-gradient(135deg, #6fd6cf, #1f8a86); }

  .site-footer {
    height: 80px; background: var(--maroon); border-top: 8px solid var(--yellow);
    display: flex; align-items: center; justify-content: space-between; padding: 0 24px; color: #fff;
  }
  .footer-art { width: 90px; height: 60px; border-radius: 4px; background: linear-gradient(135deg, #c9a23a, #5f7a2a); }
  .footer-tagline { font-family: "Fredoka", sans-serif; font-weight: 500; font-size: 18px; }
  .footer-links { display: flex; gap: 18px; font-size: 14px; font-weight: 600; }
</style>
</head>
<body>
  <header class="site-header">
    <div class="brand"><span class="brand-mark"></span><span class="brand-name">Arcadia Mini</span></div>
    <nav class="main-nav"><a href="#">Home</a><a href="#">New</a><a href="#">Popular</a><a href="#">Categories</a></nav>
  </header>

  <section class="hero" role="img" aria-label="Colourful game artwork of a purple fantasy world for the featured release">
    <div class="hero-copy">
      <span class="hero-tag">NEW RELEASE</span>
      <h1 class="hero-title">Orbwhistle Isle</h1>
      <span class="hero-btn">Play Now</span>
    </div>
  </section>

  <main class="content">
    <aside class="category-list">
      <h2>Categories</h2>
      <div class="category cat-blue">Action</div>
      <div class="category cat-orange">Puzzle</div>
      <div class="category cat-green">Racing</div>
      <div class="category cat-purple">Sports</div>
      <div class="category cat-red">Arcade</div>
      <div class="category cat-teal">Adventure</div>
    </aside>

    <section class="games">
      <h2>Top Games</h2>
      <div class="game-grid">
        <article class="game-card"><div class="game-thumb t1" role="img" aria-label="Game cover art"></div><div class="game-info"><span class="game-title">Quillby Hop</span><span class="game-play">Play</span></div></article>
        <article class="game-card"><div class="game-thumb t2" role="img" aria-label="Game cover art"></div><div class="game-info"><span class="game-title">Zentor Loop</span><span class="game-play">Play</span></div></article>
        <article class="game-card"><div class="game-thumb t3" role="img" aria-label="Game cover art"></div><div class="game-info"><span class="game-title">Mossrun Bay</span><span class="game-play">Play</span></div></article>
        <article class="game-card"><div class="game-thumb t4" role="img" aria-label="Game cover art"></div><div class="game-info"><span class="game-title">Corvix Tile</span><span class="game-play">Play</span></div></article>
        <article class="game-card"><div class="game-thumb t5" role="img" aria-label="Game cover art"></div><div class="game-info"><span class="game-title">Plumy Dash</span><span class="game-play">Play</span></div></article>
        <article class="game-card"><div class="game-thumb t6" role="img" aria-label="Game cover art"></div><div class="game-info"><span class="game-title">Bramblo Jig</span><span class="game-play">Play</span></div></article>
        <article class="game-card"><div class="game-thumb t4" role="img" aria-label="Game cover art"></div><div class="game-info"><span class="game-title">Wispo Trail</span><span class="game-play">Play</span></div></article>
        <article class="game-card"><div class="game-thumb t1" role="img" aria-label="Game cover art"></div><div class="game-info"><span class="game-title">Ferro Digs</span><span class="game-play">Play</span></div></article>
        <article class="game-card"><div class="game-thumb t6" role="img" aria-label="Game cover art"></div><div class="game-info"><span class="game-title">Glim Putt</span><span class="game-play">Play</span></div></article>
        <article class="game-card"><div class="game-thumb t2" role="img" aria-label="Game cover art"></div><div class="game-info"><span class="game-title">Frosti Skid</span><span class="game-play">Play</span></div></article>
        <article class="game-card"><div class="game-thumb t5" role="img" aria-label="Game cover art"></div><div class="game-info"><span class="game-title">Embro Zoom</span><span class="game-play">Play</span></div></article>
        <article class="game-card"><div class="game-thumb t3" role="img" aria-label="Game cover art"></div><div class="game-info"><span class="game-title">Lilypo Leap</span><span class="game-play">Play</span></div></article>
      </div>
    </section>
  </main>

  <footer class="site-footer">
    <div class="footer-art" role="img" aria-label="Cartoon game character artwork"></div>
    <p class="footer-tagline">Free mini games every day</p>
    <nav class="footer-links"><span>About</span><span>Contact</span><span>Privacy</span></nav>
  </footer>
</body>
</html>
```